Med Spa business card design with logo

Need a logo design and business card for our new company Velora Skinworks Med Spa. We are a medical office that deals with high end clients. We offer them skin care products which include NERVAX, lip augmentation, and various laser for the skin. I king of like the logo attached, maybe something along those lines but also open to any logo concept.
Updates

Target Market(s)

Out target audience are male and females in the age range of 21-80 years of age

Industry/Entity Type

Medical

Contact Information for Business Card

woukd like front of card to have logo and business name VELORA SKINWORKS MEDSPA. Back of card employee name and phone number along with instagram logo and user name

Font styles to use
Serif
Sans Serif

Requirements
Must have
• prefer monochromatic look white, black, gold
Should not have
• not too colorful

```html
<!DOCTYPE html>
<html lang="en">
<head>
<meta charset="utf-8">
<title>Velora Skinworks Med Spa – Business Card</title>
<link rel="stylesheet" href="https://fonts.googleapis.com/css2?family=Josefin+Sans:wght@400;600&family=Lato:wght@400;700&display=swap">
<style>
  :root {
    --canvas-bg: #ecebea;
    --frost-top: #f7f5f4;
    --frost-bottom: #e9e4e2;
    --band-dark: #1c1d20;
    --band-dark-edge: #2c2d31;
    --ink-dark: #2b2b2b;
    --ink-light: #ffffff;
    --rule-light: rgba(255,255,255,0.22);
    --mark-grey: #7c7a78;
  }
  * { margin: 0; padding: 0; box-sizing: border-box; }
  html, body { width: 1200px; height: 900px; overflow: hidden; }
  body { background: var(--canvas-bg); position: relative; font-family: "Lato", sans-serif; }

  .card {
    position: absolute;
    width: 556px;
    height: 345px;
    border-radius: 30px;
    overflow: hidden;
    box-shadow: 0 10px 30px rgba(0,0,0,0.18);
  }
  .card--front { left: 238px; top: 60px; }
  .card--back  { left: 459px; top: 520px; }

  .brand-band {
    height: 166px;
    background: linear-gradient(180deg, var(--frost-top), var(--frost-bottom));
    display: flex;
    flex-direction: column;
    align-items: center;
    padding-top: 28px;
  }
  .brand-mark {
    width: 64px; height: 64px;
    border-radius: 50%;
    background: var(--mark-grey);
  }
  .brand-name {
    margin-top: 24px;
    font-family: "Josefin Sans", sans-serif;
    font-size: 20px;
    letter-spacing: 1px;
    color: var(--ink-dark);
    line-height: 1;
  }
  .brand-sub {
    margin-top: 4px;
    display: flex;
    align-items: center;
    gap: 8px;
    font-family: "Josefin Sans", sans-serif;
    font-size: 9px;
    letter-spacing: 4px;
    color: var(--ink-dark);
  }
  .brand-sub::before, .brand-sub::after {
    content: "";
    width: 72px; height: 1px;
    background: var(--ink-dark);
  }

  .info-band {
    height: 179px;
    background: linear-gradient(180deg, var(--band-dark), var(--band-dark-edge) 60%, var(--band-dark));
    color: var(--ink-light);
    text-align: center;
    padding-top: 14px;
  }
  .person-name { font-weight: 700; font-size: 18px; letter-spacing: 0.5px; line-height: 22px; }
  .person-title { font-size: 15px; letter-spacing: 0.5px; line-height: 18px; }
  .rule { width: 290px; height: 1px; background: var(--rule-light); margin: 8px auto; }
  .rule--lower { margin: 5px auto 7px; }
  .contact-row {
    display: flex; justify-content: center; align-items: center; gap: 6px;
    font-size: 14px; line-height: 22px;
  }
  .contact-row svg { width: 12px; height: 12px; fill: var(--ink-light); }
  .divider { width: 1px; height: 18px; background: var(--ink-light); margin: 0 3px; }
  .social-square { width: 11px; height: 11px; border: 1.5px solid var(--ink-light); border-radius: 2px; }
  .address { font-size: 14px; line-height: 18px; }

  .pattern-band {
    height: 179px;
    background: linear-gradient(180deg, #202124, #2a2b2e 50%, #1d1e21);
  }
</style>
</head>
<body>

  <section class="card card--front">
    <div class="brand-band">
      <div class="brand-mark"></div>
      <div class="brand-name">VELORA SKINWORKS</div>
      <div class="brand-sub">MEDSPA</div>
    </div>
    <div class="info-band">
      <div class="person-name">MARCUS ELLINGTON</div>
      <div class="person-title">PRESIDENT</div>
      <div class="rule"></div>
      <div class="contact-row">
        <svg viewBox="0 0 16 16" aria-hidden="true"><path d="M3 1h3l1.5 4-2 1.3a9 9 0 0 0 4.2 4.2L11 8.5l4 1.5v3a2 2 0 0 1-2 2A13 13 0 0 1 1 3a2 2 0 0 1 2-2z"/></svg>
        <span>972.555.0148</span>
        <span class="divider"></span>
        <svg viewBox="0 0 16 16" aria-hidden="true"><path d="M1 3h14v10H1z M2 4l6 5 6-5" fill="var(--ink-light)" stroke="var(--band-dark)" stroke-width="1.2"/></svg>
        <span>hello@veloraskin.com</span>
      </div>
      <div class="contact-row">
        <span class="social-square"></span>
        <span>/veloraskinworksmedspa</span>
      </div>
      <div class="rule rule--lower"></div>
      <div class="address">2400 Willow Crest Lane Harlow, TX 75310</div>
    </div>
  </section>

  <section class="card card--back">
    <div class="brand-band">
      <div class="brand-mark"></div>
      <div class="brand-name">VELORA SKINWORKS</div>
      <div class="brand-sub">MEDSPA</div>
    </div>
    <div class="pattern-band" role="img" aria-label="Repeating tone-on-tone brand monogram pattern on dark background"></div>
  </section>

</body>
</html>
```